Webdesign für Importeur von Tierbedarfsartikeln
Zielgruppe
Wir importieren Tierbedarfsartikel und verkaufen sie ausschließlich online. Zielgruppe sind in erster Linie Katzenhalter.
Aufgabenstellung
Es gibt eine bestehende Webseite www.pfotenhain24.de Sie wurde bei Webrono erstellt und ist aktiv. Die Seite soll eine professionelle Ansicht erhalten. Schön wären edle Farben, nicht kunterbunt. Wichtig in dem Zusammenhang ist eben, dass sich derjenige mit dem Webronokonzept auskennt.
Dieser Auftrag wird Folgeaufträge erhalten, sprich Logo, Werbeflyer usw. Bilder der Produkte sind vorhanden.

```html
<!DOCTYPE html>
<html lang="de">
<head>
<meta charset="utf-8">
<title>Pfotenhain24</title>
<link href="https://fonts.googleapis.com/css2?family=Lato:wght@300;400;700&display=swap" rel="stylesheet">
<style>
:root{
  --blue:#2337ec;
  --blue-dark:#1a2bd0;
  --nav-bg:#eef0f8;
  --nav-active:#5b7fd6;
  --text:#222;
  --muted:#777;
  --price:#d9534f;
  --border:#d8d8d8;
  --label-bg:#f1f1f1;
  --stock:#f0b400;
}
*{box-sizing:border-box;margin:0;padding:0}
html,body{width:1200px;height:2486px;overflow:hidden;background:#fff;font-family:'Lato',sans-serif;color:var(--text)}
.page{position:relative;width:1200px;height:2486px}
.abs{position:absolute}
.header{left:0;top:0;width:1200px;height:94px;background:var(--blue)}
.logo{left:150px;top:48px;color:#fff;font-size:30px;font-weight:400;display:flex;align-items:center;gap:8px;border-bottom:2px solid #fff;padding-bottom:2px}
.logo .dot{width:14px;height:14px;border-radius:50%;background:#fff}
.topnote{top:12px;color:#fff;font-size:10px;display:flex;align-items:center;gap:6px}
.search{left:574px;top:40px;width:367px;height:34px;background:#fff;border-radius:2px;font-size:10px;color:#999;padding:11px 14px}
.search svg{position:absolute;right:12px;top:10px}
.icon-user{left:977px;top:48px}
.icon-cart{left:1016px;top:48px;color:#fff;font-size:9px}
.nav{left:0;top:94px;width:1200px;height:43px;background:var(--nav-bg)}
.nav ul{list-style:none;display:flex;position:absolute;left:148px;top:0;height:43px}
.nav li{font-size:10.5px;font-weight:700;color:#333;padding:0 16px;line-height:43px;letter-spacing:.2px}
.nav li.active{background:var(--nav-active);color:#fff}
.hero{left:0;top:137px;width:1200px;height:413px;background:linear-gradient(90deg,#6fb6d8 0%,#8cc6df 50%,#a9cfe0 100%)}
.hero-cat{left:690px;top:137px;width:510px;height:413px;background:radial-gradient(ellipse at 60% 45%,#8e9196 0%,#a3a9ae 45%,rgba(169,207,224,0) 75%)}
.hero-snake{left:340px;top:370px;width:420px;height:170px;background:radial-gradient(ellipse at 50% 55%,rgba(228,76,66,.75) 0%,rgba(228,76,66,.25) 45%,rgba(228,76,66,0) 70%)}
.hero h1{left:150px;top:252px;color:#fff;font-size:35px;font-weight:700}
.hero-text{left:150px;top:310px;width:520px;color:#fff;font-size:14px;line-height:23px}
.btn{left:150px;top:374px;width:185px;height:43px;background:var(--blue);color:#fff;font-size:14px;font-weight:700;display:flex;align-items:center;justify-content:center;gap:10px;border-radius:2px}
.h2{left:0;width:1200px;text-align:center;color:var(--blue);font-size:24px;font-weight:700}
.quote{left:183px;top:647px;width:360px;border-left:3px solid var(--blue);padding-left:24px;color:var(--blue);font-size:25px;font-weight:300;line-height:30px}
.intro{left:620px;top:645px;width:380px;font-size:13px;line-height:23px;color:#222}
.rule{left:0;top:813px;width:1200px;height:1px;background:#e8e8e8}
.card{width:276px;height:248px;border:1px solid var(--border);background:#fff}
.card .img{position:absolute;left:0;top:0;width:100%;height:205px}
.card .label{position:absolute;left:0;bottom:0;width:100%;height:42px;background:var(--label-bg);border-top:1px solid var(--border);text-align:center;line-height:42px;font-size:13px}
.slide{top:1625px;height:309px}
.arrow{width:45px;height:45px;border-radius:50%;background:var(--blue);top:1747px}
.arrow svg{position:absolute;left:14px;top:12px}
.sale{top:2044px;height:255px;border:1px solid var(--border);background:#fff}
.sale .img{position:absolute}
.sale h3{position:absolute;color:var(--blue);font-size:16px;font-weight:700;line-height:18px}
.sale .line{position:absolute;width:48px;height:2px;background:#222}
.sale .price{position:absolute;font-size:19px;color:var(--price)}
.sale .price s{color:#888;margin-left:8px}
.sale .stock{position:absolute;font-size:15px;line-height:18px;padding-left:20px}
.sale .stock:before{content:"";position:absolute;left:2px;top:6px;width:7px;height:7px;border-radius:50%;background:var(--stock)}
.footer{left:0;top:2368px;width:1200px;height:43px;background:var(--blue);color:#fff;font-size:11.5px}
.footer span{position:absolute;top:14px}
.pay{left:0;top:2437px;width:1200px;display:flex;justify-content:center;gap:22px;font-size:13px;font-weight:700;color:#444}
.pay span{display:flex;align-items:center;gap:5px}
.pay i{width:9px;height:9px;background:#444;display:inline-block}
</style>
</head>
<body>
<div class="page">
  <header class="abs header">
    <div class="abs logo"><span class="dot"></span>Pfotenhain24</div>
    <div class="abs topnote" style="left:574px">
      <svg width="16" height="10" viewBox="0 0 16 10"><rect x="0.5" y="0.5" width="15" height="9" fill="none" stroke="#fff"/><circle cx="8" cy="5" r="2.2" fill="#fff"/></svg>
      Gutscheincode "Plüsch" und 15% auf alle Kuschelbetten sichern
    </div>
    <div class="abs topnote" style="left:898px">
      <svg width="11" height="11" viewBox="0 0 11 11"><path d="M5.5 1 10 3v5L5.5 10 1 8V3z" fill="none" stroke="#fff"/></svg>
      Kostenloser Versand ab €65,00
    </div>
    <div class="abs search">Suche...
      <svg width="12" height="12" viewBox="0 0 12 12"><circle cx="5" cy="5" r="3.8" fill="none" stroke="#999" stroke-width="1.3"/><path d="M8 8l3 3" stroke="#999" stroke-width="1.3"/></svg>
    </div>
    <svg class="abs icon-user" width="20" height="20" viewBox="0 0 20 20"><circle cx="10" cy="10" r="9" fill="none" stroke="#fff" stroke-width="1.6"/><circle cx="10" cy="8" r="3.3" fill="#fff"/><path d="M4.5 16c1.5-3 9.5-3 11 0" fill="#fff"/></svg>
    <div class="abs icon-cart">
      <svg width="22" height="18" viewBox="0 0 22 18"><path d="M1 2h3l2.5 10h11l2-7H5" fill="none" stroke="#fff" stroke-width="1.7"/><circle cx="8" cy="15.5" r="1.6" fill="#fff"/><circle cx="16" cy="15.5" r="1.6" fill="#fff"/></svg>
      <span style="position:absolute;left:21px;top:-3px">(0)</span>
    </div>
  </header>

  <nav class="abs nav">
    <ul>
      <li class="active">PFOTENHAIN24</li>
      <li>KATZENKRATZARTIKEL</li>
      <li>PLÜSCHBETTEN</li>
      <li>KATZENSPIELZEUG</li>
      <li>INTERAKTIVE SPIELZEUGE</li>
      <li>ZUBEHÖR</li>
      <li>SALE</li>
      <li>KONTAKT</li>
    </ul>
  </nav>

  <section class="abs hero" role="img" aria-label="Graue Katze pirscht sich an eine rot-schwarze Spielzeugschlange heran"></section>
  <div class="abs hero-cat"></div>
  <div class="abs hero-snake"></div>
  <div class="hero"><h1 class="abs" style="left:150px;top:252px;color:#fff;font-size:35px;font-weight:700">Willkommen bei Pfotenhain24.de</h1></div>
  <p class="abs hero-text">Hier findest Du eine liebevoll zusammengestellte Auswahl an Zubehör für deine vierbeinigen Familienmitglieder.</p>
  <div class="abs btn">
    <svg width="20" height="16" viewBox="0 0 22 18"><path d="M1 2h3l2.5 10h11l2-7H5" fill="none" stroke="#fff" stroke-width="1.8"/><circle cx="8" cy="15.5" r="1.6" fill="#fff"/><circle cx="16" cy="15.5" r="1.6" fill="#fff"/></svg>
    Jetzt einkaufen
  </div>

  <h2 class="abs h2" style="top:582px">Willkommen bei Pfotenhain24.de</h2>
  <blockquote class="abs quote">Hier findest Du eine liebevoll zusammengestellte Auswahl an Zubehör für deine vierbeinigen Familienmitglieder.</blockquote>
  <div class="abs intro">
    <p>Unsere Artikel wurden durch unser qualifiziertes, flauschiges Fachpersonal auf Haltbarkeit und Spielspaß geprüft und sind mit schnurrigen Grüßen zu empfehlen!</p>
    <p style="margin-top:22px">Schön, dass du da bist!</p>
  </div>
  <div class="abs rule"></div>

  <h2 class="abs h2" style="top:889px">Unsere Produkte</h2>
  <div class="abs card" style="left:150px;top:946px">
    <div class="img" role="img" aria-label="Kratzsofa aus Pappe mit liegender Katze" style="background:radial-gradient(ellipse at 50% 55%,#3f7f86 0%,#b58a4a 45%,#fff 72%)"></div>
    <div class="label">KATZENKRATZARTIKEL</div>
  </div>
  <div class="abs card" style="left:462px;top:946px">
    <div class="img" role="img" aria-label="Rosa Plüschbett" style="background:radial-gradient(circle at 50% 50%,#f3d3dc 0%,#f8e2e8 45%,#fff 70%)"></div>
    <div class="label">PLÜSCHBETTEN</div>
  </div>
  <div class="abs card" style="left:775px;top:946px">
    <div class="img" role="img" aria-label="Graue Filzhöhle für Katzen" style="background:radial-gradient(ellipse at 50% 50%,#6b6d72 0%,#8b8d92 45%,#fff 72%)"></div>
    <div class="label">KATZENSPIELZEUG</div>
  </div>
  <div class="abs card" style="left:307px;top:1230px">
    <div class="img" role="img" aria-label="Rot-schwarze interaktive Spielzeugschlange" style="background:radial-gradient(ellipse at 50% 50%,#e34c45 0%,#ef8a84 38%,#fff 70%)"></div>
    <div class="label">INTERAKTIVE SPIELZEUGE</div>
  </div>
  <div class="abs card" style="left:618px;top:1230px">
    <div class="img" role="img" aria-label="Fusselbürste mit Holzgriff" style="background:radial-gradient(ellipse at 50% 55%,#d8b58a 0%,#e8dccb 35%,#fff 65%)"></div>
    <div class="label">ZUBEHÖR</div>
  </div>

  <h2 class="abs h2" style="top:1568px">Top-Produkte</h2>
  <div class="abs slide" style="left:150px;width:445px;background:linear-gradient(135deg,#213a33 0%,#2f6a70 50%,#c9a36a 100%)" role="img" aria-label="Katze schläft auf einem Kratzsofa"></div>
  <div class="abs slide" style="left:612px;width:438px;background:linear-gradient(160deg,#f4d6d4 0%,#eccaa2 50%,#e9c08e 100%)" role="img" aria-label="Spielzeugschlange auf Holzboden"></div>
  <div class="abs arrow" style="left:91px"><svg width="16" height="20" viewBox="0 0 16 20"><path d="M11 2 3 10l8 8" fill="none" stroke="#fff" stroke-width="2"/></svg></div>
  <div class="abs arrow" style="left:1065px"><svg width="16" height="20" viewBox="0 0 16 20"><path d="M5 2l8 8-8 8" fill="none" stroke="#fff" stroke-width="2"/></svg></div>

  <h2 class="abs h2" style="top:1987px">Sale</h2>
  <div class="abs sale" style="left:150px;width:445px">
    <div class="img" role="img" aria-label="Kratzsofa aus Pappe" style="left:22px;top:24px;width:225px;height:120px;background:radial-gradient(ellipse at 50% 50%,#7d7268 0%,#a39a90 45%,#fff 72%)"></div>
    <h3 style="left:266px;top:44px;width:170px">Kratzsofa Deluxe L 600 x B 280 x H230mm mit leichten Dellen</h3>
    <div class="line" style="left:266px;top:104px"></div>
    <div class="price" style="left:268px;top:125px">19,99 €<s>25,99 €</s></div>
    <div class="stock" style="left:268px;top:165px">Nur noch wenige<br>vorrätig</div>
  </div>
  <div class="abs sale" style="left:612px;width:437px">
    <div class="img" role="img" aria-label="Kratzball auf Holzgestell" style="left:40px;top:12px;width:180px;height:230px;background:radial-gradient(ellipse at 50% 40%,#b99f7a 0%,#7a5440 40%,#fff 72%)"></div>
    <h3 style="left:256px;top:30px;width:170px">Kratzball mit leichten optischen Mängeln</h3>
    <div class="line" style="left:256px;top:86px"></div>
    <div class="price" style="left:258px;top:110px">19,99 €<s>25,99 €</s></div>
    <div class="stock" style="left:258px;top:150px">Nur noch wenige<br>vorrätig</div>
  </div>

  <footer class="abs footer">
    <span style="left:162px">Impressum</span>
    <span style="left:275px">Datenschutzerklärung</span>
    <span style="left:442px">Cookie-Richtlinie</span>
    <span style="left:584px">Zahlung &amp; Versand</span>
    <span style="left:733px">Allgemeine Geschäftsbedingungen</span>
    <span style="left:960px">Widerrufsrecht</span>
  </footer>
  <div class="abs pay">
    <span>Paketflink</span>
    <span><i></i>Girokarte</span>
    <span>Kartix</span>
    <span>Zahlfix</span>
    <span><i></i>Ameron</span>
    <span>Kreditra</span>
  </div>
</div>
</body>
</html>
```